Fiber to the Home Business - Coming Soon Postcard

Corvalane Communications is looking for a postcard design that we can mail out to potential customers in areas that we are building our Fiber Optic network. The wording on this postcard needs to include:
Fiber Internet, Phone, HD TV.
Coming soon to your area.
Contact us now to schedule.
(252) 555-0193
Brastowee.com/fiber
Back of postcard:
Mailing information area.
Keep your same phone number
Unlimited Nationwide Long Distance
All for $19.99/month
Internet Speeds up to 150Mbps
Starting at $39.99/month
High Definition TV
Packages starting at $50/month
No Contract Required.
Industry/Entity Type
Internet Service Provider
Requirements
Must have
- Catchy background graphics on front of postcard geared toward happy internet customers.
Should not have
- Cable

```html
<!DOCTYPE html>
<html lang="en">
<head>
<meta charset="utf-8">
<title>Corvalane Communications – Fiber Coming Soon Postcard</title>
<link href="https://fonts.googleapis.com/css2?family=Oswald:wght@500;600;700&family=Saira+Semi+Condensed:wght@600;700&family=Open+Sans:wght@400;600&display=swap" rel="stylesheet">
<style>
  :root {
    --backdrop: #4f5152;
    --card: #ffffff;
    --blue: #1769c2;
    --blue-deep: #0b4f9c;
    --blue-light: #2a8fe0;
    --silver: #d9dadc;
    --silver-dark: #8e9093;
    --ink: #1c1c1c;
    --ink-soft: #555b62;
    --brand: #5b6671;
    --headline-blue: #1463b8;
  }
  * { box-sizing: border-box; margin: 0; padding: 0; }
  html, body { width: 900px; height: 1200px; overflow: hidden; }
  body { background: var(--backdrop); position: relative; font-family: "Open Sans", sans-serif; }

  .postcard { position: absolute; background: var(--card); overflow: hidden; box-shadow: 0 4px 14px rgba(0,0,0,.35); }
  .postcard__art { position: absolute; inset: 0; }

  /* Front */
  .front { left: 120px; top: 52px; width: 688px; height: 535px; }
  .front__services {
    position: absolute; left: 48px; top: 265px; width: 250px; text-align: center;
    font-family: "Oswald", sans-serif; font-weight: 600; color: #fff;
    font-size: 31px; line-height: 36px; letter-spacing: .2px;
  }
  .front__soon {
    position: absolute; left: 35px; top: 385px; width: 275px; height: 28px;
    background: linear-gradient(#9c9ea1, #6f7174); color: #111;
    font-family: "Open Sans", sans-serif; font-weight: 600; font-size: 13px;
    line-height: 28px; text-align: center;
  }
  .front__contact { position: absolute; left: 76px; top: 428px; color: #fff; font-size: 13px; }
  .front__cta { font-weight: 600; margin-bottom: 18px; }
  .contact-line { display: flex; align-items: center; gap: 4px; font-weight: 600; line-height: 18px; }
  .contact-line svg { width: 11px; height: 11px; flex: none; }
  .front__brand {
    position: absolute; left: 410px; top: 470px; width: 190px; text-align: center;
    font-family: "Oswald", sans-serif; font-weight: 500; font-size: 21px; line-height: 24px; color: var(--brand);
  }

  /* Back */
  .back { left: 118px; top: 620px; width: 690px; height: 537px; }
  .offer { position: absolute; left: 0; width: 378px; text-align: center;
    font-family: "Saira Semi Condensed", sans-serif; font-weight: 700; font-variant: small-caps; color: var(--ink); }
  .offer--headline { top: 44px; font-variant: normal; font-size: 25px; color: var(--headline-blue); letter-spacing: .3px; }
  .offer--line { font-size: 19px; }
  .offer--price { font-size: 20px; }
  .offer--price .amount { font-family: "Oswald", sans-serif; font-variant: normal; font-size: 30px; font-weight: 700; }
  .back__contact { position: absolute; left: 22px; top: 432px; color: var(--ink-soft); font-size: 11.5px; }
  .back__contact .contact-line { font-weight: 400; line-height: 14px; margin-bottom: 8px; align-items: flex-start; gap: 9px; }
  .back__contact .contact-line svg { margin-top: 2px; }
  .back__brand {
    position: absolute; left: 205px; top: 474px; width: 150px; text-align: center;
    font-family: "Oswald", sans-serif; font-weight: 500; font-size: 15px; line-height: 18px; color: var(--brand);
  }
  .mail__stamp { position: absolute; left: 593px; top: 111px; width: 62px; height: 62px; border: 1.5px solid #222; }
  .mail__line { position: absolute; left: 447px; width: 227px; height: 0; border-top: 1.5px solid #222; }
</style>
</head>
<body>

<section class="postcard front">
  <svg class="postcard__art" viewBox="0 0 688 535" width="688" height="535">
    <defs>
      <linearGradient id="photoTone" x1="0" y1="0" x2="1" y2="1">
        <stop offset="0" stop-color="#e6ecf1"/><stop offset=".45" stop-color="#8d9cab"/><stop offset="1" stop-color="#c9a7b4"/>
      </linearGradient>
      <linearGradient id="panelBlue" x1="0" y1="0" x2="1" y2="0">
        <stop offset="0" stop-color="#0c55a8"/><stop offset=".6" stop-color="#1e7bd4"/><stop offset="1" stop-color="#0b4f9c"/>
      </linearGradient>
      <linearGradient id="silverSweep" x1="0" y1="0" x2="0" y2="1">
        <stop offset="0" stop-color="#f2f2f3"/><stop offset="1" stop-color="#bfc1c4"/>
      </linearGradient>
    </defs>
    <rect width="688" height="390" fill="url(#photoTone)" role="img" aria-label="Photo of a smiling family on a sofa looking at a laptop together"/>
    <path d="M0 330 C180 300 420 350 688 300 L688 535 L0 535 Z" fill="url(#silverSweep)"/>
    <path d="M290 340 C430 380 560 360 688 330 L688 350 C560 385 420 400 290 370 Z" fill="#9a9ca0"/>
    <path d="M470 372 C570 360 640 330 688 262 L688 385 C620 395 540 395 470 372 Z" fill="var(--blue-light)"/>
    <path d="M48 208 C110 185 170 225 230 200 C260 190 285 195 298 205 L298 535 L48 535 Z" fill="url(#panelBlue)"/>
  </svg>

  <h1 class="front__services">FIBER INTERNET<br>PHONE<br>HD TV</h1>
  <p class="front__soon">COMING SOON TO YOUR AREA</p>
  <div class="front__contact">
    <p class="front__cta">Contact us now to schedule</p>
    <p class="contact-line">
      <svg viewBox="0 0 24 24"><path fill="#fff" d="M6.6 10.8a15 15 0 0 0 6.6 6.6l2.2-2.2a1 1 0 0 1 1-.25 11.4 11.4 0 0 0 3.6.57 1 1 0 0 1 1 1V20a1 1 0 0 1-1 1A17 17 0 0 1 3 4a1 1 0 0 1 1-1h3.5a1 1 0 0 1 1 1c0 1.25.2 2.45.57 3.57a1 1 0 0 1-.25 1z"/></svg>
      (252) 555-0193
    </p>
    <p class="contact-line">
      <svg viewBox="0 0 24 24"><circle cx="12" cy="12" r="10" fill="none" stroke="#fff" stroke-width="2.4"/><path d="M2 12h20M12 2c3 3 3 17 0 20M12 2c-3 3-3 17 0 20" fill="none" stroke="#fff" stroke-width="2"/></svg>
      Brastowee.com/fiber
    </p>
  </div>
  <p class="front__brand">Corvalane Communications</p>
</section>

<section class="postcard back">
  <svg class="postcard__art" viewBox="0 0 690 537" width="690" height="537">
    <defs>
      <radialGradient id="globeTone" cx=".45" cy=".35" r=".7">
        <stop offset="0" stop-color="#ffffff"/><stop offset=".5" stop-color="#d4d6d9"/><stop offset="1" stop-color="#a8abae"/>
      </radialGradient>
      <linearGradient id="bandBlue" x1="0" y1="0" x2="1" y2="0">
        <stop offset="0" stop-color="#0d5bb0"/><stop offset=".55" stop-color="#2a8be0"/><stop offset="1" stop-color="#0b4f9c"/>
      </linearGradient>
      <linearGradient id="bandSilver" x1="0" y1="0" x2="0" y2="1">
        <stop offset="0" stop-color="#a9abae"/><stop offset="1" stop-color="#e6e7e8"/>
      </linearGradient>
    </defs>
    <rect width="378" height="200" fill="url(#globeTone)" role="img" aria-label="Faint technology globe with network light streaks"/>
    <path d="M0 200 C110 175 250 150 378 170 L378 330 L0 330 Z" fill="#c9cbce"/>
    <path d="M0 205 C120 185 260 165 378 180 L378 330 L0 330 Z" fill="url(#bandBlue)"/>
    <rect y="330" width="378" height="90" fill="url(#bandSilver)"/>
    <path d="M0 420 L378 420 L378 445 C260 415 120 430 0 412 Z" fill="#ffffff"/>
    <rect y="412" width="378" height="125" fill="#ffffff"/>
    <path d="M0 412 C120 430 260 415 378 445 L378 448 C260 420 120 434 0 416 Z" fill="#d5d6d8"/>
  </svg>

  <h2 class="offer offer--headline">NO CONTRACT REQUIRED</h2>
  <p class="offer offer--line" style="top:96px">Unlimited Nationwide Long Distance</p>
  <p class="offer offer--price" style="top:126px">All for <span class="amount">$19.99</span> / month</p>
  <p class="offer offer--line" style="top:228px">Internet Speeds up to 150Mbps</p>
  <p class="offer offer--price" style="top:256px">Starting at <span class="amount">$39.99</span> / month</p>
  <p class="offer offer--line" style="top:344px">High Definition TV</p>
  <p class="offer offer--price" style="top:372px">Packages starting at <span class="amount">$50</span> / month</p>

  <div class="back__contact">
    <p class="contact-line">
      <svg viewBox="0 0 24 24"><path fill="var(--blue)" d="M12 2a7 7 0 0 0-7 7c0 5 7 13 7 13s7-8 7-13a7 7 0 0 0-7-7zm0 9.5A2.5 2.5 0 1 1 12 6.5a2.5 2.5 0 0 1 0 5z"/></svg>
      <span>2240-B Marrowfield Rd<br>Ellisburg, NC 28599</span>
    </p>
    <p class="contact-line">
      <svg viewBox="0 0 24 24"><path fill="var(--blue)" d="M6.6 10.8a15 15 0 0 0 6.6 6.6l2.2-2.2a1 1 0 0 1 1-.25 11.4 11.4 0 0 0 3.6.57 1 1 0 0 1 1 1V20a1 1 0 0 1-1 1A17 17 0 0 1 3 4a1 1 0 0 1 1-1h3.5a1 1 0 0 1 1 1c0 1.25.2 2.45.57 3.57a1 1 0 0 1-.25 1z"/></svg>
      (252) 555-0193
    </p>
    <p class="contact-line">
      <svg viewBox="0 0 24 24"><circle cx="12" cy="12" r="7" fill="var(--blue)"/></svg>
      Brastowee.com/fiber
    </p>
  </div>
  <p class="back__brand">Corvalane Communications</p>

  <div class="mail__stamp"></div>
  <div class="mail__line" style="top:292px"></div>
  <div class="mail__line" style="top:319px"></div>
  <div class="mail__line" style="top:348px"></div>
</section>

</body>
</html>
```